Modern and Improved business card design for Family Dental Practice

We have 2 sets of logo we have designed and now just need a business card layout and design for the office. Colors are on the logo. We can choose which logo we want to go with . The font can be changed to whatever seems modern and relevant. We are family dental office that has been open for over 15 years in South Austin Texas.

Target Market(s)

Handout Business cards to referrals and specialists

Industry/Entity Type

Dental

Contact Information for Business Card

We need address, phone, website and email address. 4830 North Maple Loop Suite 208 , Austin,Texas 78392....phone: 512-847-3195.....email- info@bluepinedental.example....website - BluePineDental.example

Font styles to use
Serif
Decorative

Requirements
Must have
• my logo. We have 2 logos, but we can use just one or if we can incorporate one on one side and the other on the other side.
Nice to have
• Really just need a modern look and clean that incorporates the logo and colors .

```html
<!DOCTYPE html>
<html lang="en">
<head>
<meta charset="utf-8">
<title>Blue Pine Family Dentistry – Business Card</title>
<link rel="stylesheet" href="https://fonts.googleapis.com/css2?family=Questrial&family=Arimo:wght@400&display=swap">
<style>
  :root {
    --backdrop: #a09e9f;
    --card-white: #ffffff;
    --card-dark: #1b1b1b;
    --brand-green: #066f00;
    --leaf-green: #0a7a05;
    --pale-green: #b7c98a;
    --ink: #1a1a1a;
    --light-text: #f2f2f2;
  }
  html, body {
    margin: 0;
    width: 1075px;
    height: 1200px;
    overflow: hidden;
    background: var(--backdrop);
  }
  .card {
    position: absolute;
    left: 206px;
    width: 664px;
    height: 395px;
    box-shadow: 3px 3px 2px rgba(0, 0, 0, 0.6);
    overflow: hidden;
  }
  .card-front { top: 187px; background: var(--card-white); }
  .card-back  { top: 637px; background: var(--card-dark); }

  .wordmark {
    position: absolute;
    font-family: "Questrial", sans-serif;
    font-weight: 400;
    margin: 0;
    letter-spacing: -0.5px;
    z-index: 2;
  }
  .wordmark .tagline {
    display: block;
    color: var(--leaf-green);
    letter-spacing: 1px;
    line-height: 1.2;
  }
  .card-front .wordmark { left: 44px; top: 38px; font-size: 47px; line-height: 40px; color: var(--ink); }
  .card-front .wordmark .tagline { font-size: 16px; margin-top: 10px; }
  .card-back .wordmark  { left: 325px; top: 160px; font-size: 64px; line-height: 53px; color: var(--light-text); }
  .card-back .wordmark .tagline { font-size: 21px; margin-top: 12px; }

  .contact-band {
    position: absolute;
    left: 0;
    top: 178px;
    width: 100%;
    height: 217px;
    background: var(--brand-green);
  }
  .contact-list {
    position: absolute;
    left: 35px;
    top: 37px;
    margin: 0;
    padding: 0;
    list-style: none;
    font-family: "Arimo", sans-serif;
    font-size: 18px;
    color: var(--light-text);
    z-index: 2;
  }
  .contact-list li {
    display: flex;
    align-items: flex-start;
    gap: 6px;
    height: 23.5px;
    line-height: 23.5px;
  }
  .contact-list li.address { margin-top: 13px; height: auto; line-height: 24px; }
  .contact-list svg { width: 17px; height: 17px; margin-top: 3px; flex: none; fill: var(--light-text); }

  .brand-disc {
    position: absolute;
    border-radius: 50%;
    z-index: 1;
  }
  .card-front .brand-disc {
    left: 314px;
    top: 154px;
    width: 306px;
    height: 306px;
    background: var(--pale-green);
  }
  .card-back .brand-disc {
    left: 132px;
    top: 153px;
    width: 152px;
    height: 152px;
    background: var(--leaf-green);
  }
</style>
</head>
<body>

<section class="card card-front" aria-label="Card front">
  <h1 class="wordmark">BLUE<br>PINE<span class="tagline">FAMILY DENTISTRY</span></h1>

  <div class="contact-band">
    <ul class="contact-list">
      <li>
        <svg viewBox="0 0 24 24" aria-hidden="true"><path d="M6.6 10.8a15.1 15.1 0 0 0 6.6 6.6l2.2-2.2c.3-.3.7-.4 1-.2 1.1.4 2.3.6 3.6.6.6 0 1 .4 1 1V20c0 .6-.4 1-1 1A17 17 0 0 1 3 4c0-.6.4-1 1-1h3.5c.6 0 1 .4 1 1 0 1.3.2 2.5.6 3.6.1.3 0 .7-.2 1z"/></svg>
        <span>512-847-3195</span>
      </li>
      <li>
        <svg viewBox="0 0 24 24" aria-hidden="true"><path d="M2 5h20v14H2z M2 5l10 8 10-8" fill="none" stroke="#f2f2f2" stroke-width="2"/></svg>
        <span>info@bluepinedental.example</span>
      </li>
      <li>
        <svg viewBox="0 0 24 24" aria-hidden="true"><g fill="none" stroke="#f2f2f2" stroke-width="2"><circle cx="12" cy="12" r="9"/><ellipse cx="12" cy="12" rx="4" ry="9"/><path d="M3 12h18M5 7h14M5 17h14"/></g></svg>
        <span>BluePineDental.example</span>
      </li>
      <li class="address">
        <svg viewBox="0 0 24 24" aria-hidden="true"><path d="M12 2a7 7 0 0 0-7 7c0 5 7 13 7 13s7-8 7-13a7 7 0 0 0-7-7zm0 9.5A2.5 2.5 0 1 1 12 6.5a2.5 2.5 0 0 1 0 5z"/></svg>
        <span>4830 North Maple Loop Suite<br>208 Austin, Texas 78392</span>
      </li>
    </ul>
  </div>

  <div class="brand-disc" role="img" aria-label="Large brand mark decoration"></div>
</section>

<section class="card card-back" aria-label="Card back">
  <div class="brand-disc" aria-hidden="true"></div>
  <h2 class="wordmark">BLUE<br>PINE<span class="tagline">FAMILY DENTISTRY</span></h2>
</section>

</body>
</html>
```